Business Card Design Project - Tall Maple

We are looking for a new business card design. Our company name is Tall Maple Communication Solutions. Our primary function is to provide our clients with communication solutions. These solutions include commercial phone systems and T1 and Fiber Internet lines. Another major part of the business is cabling new buildings with CAT5 cable for both data and phone.

Industry/Entity Type

Communication

Requirements
Must have
• The cards need to be two sided and have some bleeding edge color.
Nice to have
• We are going to upload our current logo BUT we are not married to this logo. If you want to incorporate a re-designed logo with the new business card - please feel free to do so. We are looking for a new bold look that is very colorful yet professional.

```html
<!DOCTYPE html>
<html lang="en">
<head>
<meta charset="utf-8">
<title>Tall Maple – Business Card</title>
<link rel="stylesheet" href="https://fonts.googleapis.com/css2?family=Noto+Sans:wght@400;700&display=swap">
<style>
  :root {
    --navy: #102a56;
    --card: #ffffff;
    --shadow: #020c1c;
    --on-navy: #ffffff;
  }
  * { margin: 0; padding: 0; box-sizing: border-box; }
  html, body { width: 1071px; height: 1200px; overflow: hidden; background: var(--navy); }
  body { position: relative; font-family: "Noto Sans", Verdana, sans-serif; color: var(--navy); }

  .card {
    position: absolute;
    left: 86px;
    width: 900px;
    height: 514px;
    background: var(--card);
    overflow: hidden;
    box-shadow: 14px 12px 4px var(--shadow);
  }
  .card--front { top: 63px; }
  .card--back  { top: 627px; }

  .brand-name {
    position: absolute;
    font-weight: 400;
    color: var(--navy);
    white-space: nowrap;
    line-height: 1;
  }

  .card--front .brand-name { left: 77px; top: 172px; font-size: 125px; letter-spacing: -1px; }
  .tagline {
    position: absolute; left: 224px; top: 305px;
    font-size: 50px; white-space: nowrap; line-height: 1;
  }

  .card--back .brand-name { left: 169px; top: 72px; font-size: 67px; }

  .contact {
    position: absolute; left: 0; top: 188px;
    font-size: 17.5px; line-height: 20.6px; letter-spacing: 1.1px;
  }
  .contact__row { display: grid; grid-template-columns: 450px 1fr; column-gap: 21px; margin-bottom: 20.6px; }
  .contact__label { text-align: right; font-weight: 700; }

  .name-band { position: absolute; left: 0; top: 0; }
  .holder-name {
    position: absolute; left: 460px; top: 458px; width: 280px;
    text-align: center; color: var(--on-navy);
    font-weight: 700; font-size: 31px; letter-spacing: 1px; line-height: 1;
  }
</style>
</head>
<body>
  <section class="card card--front">
    <h1 class="brand-name">Tall Maple</h1>
    <p class="tagline">Communication solutions</p>
  </section>

  <section class="card card--back">
    <h2 class="brand-name">Tall Maple</h2>

    <dl class="contact">
      <div class="contact__row">
        <dt class="contact__label">Address</dt>
        <dd>1480 W Harbor Lane, Suite 210<br>Mesa, AZ&nbsp;&nbsp;85201</dd>
      </div>
      <div class="contact__row">
        <dt class="contact__label">Telephone</dt>
        <dd>480.555.0148 (Office)<br>480.555.0193 (Mobile)<br>800.555.0176 (24/7)</dd>
      </div>
      <div class="contact__row">
        <dt class="contact__label">Fax</dt>
        <dd>800.555.0124</dd>
      </div>
      <div class="contact__row">
        <dt class="contact__label">Website</dt>
        <dd>tallmaplecommunications.com</dd>
      </div>
    </dl>

    <svg class="name-band" width="900" height="514" viewBox="0 0 900 514" aria-hidden="true">
      <path d="M397 514 C397 462 420 424 480 424 L823 424 C860 424 885 405 900 381 L900 514 Z" fill="var(--navy)"/>
    </svg>
    <p class="holder-name">Owen Hartley</p>
  </section>
</body>
</html>
```